Lumo Medical Aesthetics - Service Flyer

We are looking to have a friend-fold flyer designed that outlines all of the services offered. I am able to provide pricing on all products and outline of services.

We have had a flyer made in the past and the colours were black and white to go with the logo and keep it simple. We would prefer to keep these colours, but are open to adding in a couple of extra complimentary colours which would match our clinic. I have attached the original flyer that was created as well as our logo.

Target Market(s)

Women aged 25-65

Requirements
Must have
• Our website is www.lumoclinica.example
• 555-014-2271
• Facebook: lumoclinica
• Instagram @lumoclinica
• Services to be included are:
• Some pricing has not been listed, but will update shortly
• Velanor $8/unit
• Nuvexa $10/unit
• Dermal Fillers
• (Cheeks, lips, jawline, chin, temples, under eyes, smile lines, smokers lines)
• 1ml syringe $475
• Mini Lip Plump $250
• Non-Surgical Face Lift $1100
• (Choice of 3 areas, eg. lips, jaw contouring, cheeks)
• Facial Treatments:
• Personalized Facial $85
• Organic Facial -$100
• Deep Cleansing / Acne Facial - $120
• Gel Peel (20% Glycolic/10% Lactic/3.2pH) - $75
• Dermaplaning $120
• Microdermabrasion $120
• Microneedling $250
• Microneedling (package of 3) $600
• Platelet-Rich Plasma (PRP) Facial $400
• Platinum Facial (Dermaplaning + Microneedling) $350
• LED Light Therapy $45
• High Frequency $45
• Skin Consultation (Free)
• Permanent Make-Up:
• Microblading $350
• Microblading Touch-Up $50
• Lashline Enhancement - Top Lashline $300
• Lashline Enhancement - Bottom Lashline $350
• Touch-Up Top/Bottom Lashline $50
• Lip Blush $450
• Lip Blush Touch-up $50
• Tattoo Removal $200 (per session)
• Cosmetic Treatments:
• Classic Eyelash Extensions $99
• Classic Fill $45
• Hybrid Eyelash Extensions $120
• Hybrid Fill $55
• Eyelash Lift & Tint $75
• Teeth Whitening $125
• Organic Teeth Whitening $150
• Medical Aesthetics Treatments:
• Laser Hair Removal $35 and up (per session)
• (Consultation and patch test required for all clients)
• Microneedling for Stretch Marks and Scars - $250 +
• Platelet-Rich Plasma (PRP) Hair Restoration - $500
• Scalp Micropigmentation - $500 and up
• The fernpulse / laser hair removal write-up should be replaced with the following:
• We believe in providing only the best for our clients. We specialize in a number of Medical Aesthetics Treatments to address common skin and anti-aging concerns among our clients. All of our treatments are non-invasive, highly effective and affordable. Our services are performed by certified professionals, using clinically proven equipment and products approved and certified through Civic Care Bureau.
• We take pride in the high calibre experience we offer our clients and believe that choosing the appropriate certified professional that can deliver the results you desire, is of primary importance. Lumo employs highly qualified professionals, operating under Dr. Daniel Okafor, Board Certified Plastic Surgeon acting as the Medical Director, as well as partners of the Harbourline Medical team.

```html
<!DOCTYPE html>
<html lang="en">
<head>
<meta charset="utf-8">
<title>Lumo Medical Aesthetics – Service Flyer</title>
<link rel="stylesheet" href="https://fonts.googleapis.com/css2?family=Oswald:wght@400;500&family=Open+Sans:wght@400;600&display=swap">
<style>
:root{
  --stage:#d3d4d6;
  --paper:#ffffff;
  --slate:#606062;
  --slate-dark:#535355;
  --blush:#e3b8ae;
  --blush-deep:#c88f85;
  --ink:#3d3d3f;
  --ink-soft:#555557;
  --rule:#9a9a9c;
}
*{box-sizing:border-box;margin:0;padding:0}
html,body{width:878px;height:1200px;overflow:hidden;background:var(--stage)}
body{position:relative;font-family:"Open Sans",Arial,sans-serif;color:var(--ink)}
.sheet{position:absolute;left:57px;width:751px;height:530px;display:grid;grid-template-columns:repeat(3,1fr);background:var(--paper);box-shadow:3px 4px 6px rgba(0,0,0,.35)}
.sheet--outside{top:41px}
.sheet--inside{top:622px}
.panel{position:relative;overflow:hidden}
.panel--slate{background:var(--slate);color:#fff}
.band{position:absolute;left:0;right:0;top:491px;height:28px;background:var(--blush);display:flex;align-items:center;justify-content:center;font-size:13px;color:#222;gap:6px}
.band--deep{background:#dcaaa0}
.photo{position:absolute;display:block}
.heading{font-family:"Oswald","Arial Narrow",sans-serif;font-weight:400;text-transform:uppercase;letter-spacing:.2px}
.copy{font-size:9.4px;line-height:12.6px;color:var(--ink-soft)}
.copy p+p{margin-top:13px}
.justify{text-align:justify}

/* outside */
.intro{position:absolute;top:250px;left:15px;right:14px}
.intro .heading{font-size:14.5px;color:var(--ink);margin-bottom:17px;letter-spacing:.4px}
.contact{position:absolute;top:186px;left:20px;right:20px;text-align:center}
.contact .heading{font-size:14.5px;margin-bottom:20px}
.contact .copy{color:#f2f2f2;font-size:9.3px;line-height:11.8px}
.contact-rule{position:absolute;top:352px;left:35px;right:35px;border-top:1px solid #8d8d8f}
.team{position:absolute;top:371px;left:0;right:0;text-align:center;font-size:9.4px;line-height:14.5px;color:#f2f2f2}
.more{position:absolute;top:423px;left:0;right:0;text-align:center;font-size:11px;line-height:18px;color:#f2f2f2}
.social{position:absolute;top:469px;left:0;right:0;display:flex;justify-content:center;gap:14px;font-size:9.2px;color:#f2f2f2}
.social span::before{content:"";display:inline-block;width:6px;height:6px;border-radius:50%;background:var(--blush);margin-right:5px;vertical-align:middle}
.brand{display:flex;flex-direction:column;align-items:flex-end;font-family:"Open Sans",Arial,sans-serif;font-weight:400;color:#1f1f21;line-height:1}
.brand--cover{position:absolute;top:30px;right:16px;text-align:right}
.brand .brand-name{font-size:35px;letter-spacing:1px}
.brand .brand-sub{font-size:14px;letter-spacing:1.5px;margin-top:3px}
.brand--light{color:#fff;position:absolute;top:16px;left:0;right:0;align-items:center}
.brand--light .brand-name{font-size:23px}
.brand--light .brand-sub{font-size:9.5px;margin-top:2px}
.tagline{position:absolute;top:420px;left:10px;right:10px;text-align:center;font-size:14.5px;line-height:20px;color:#2c2c2e}

/* inside */
.menu{position:absolute;left:15px;right:14px}
.menu .heading{font-size:11.5px;color:var(--blush-deep);margin-bottom:7px}
.menu--light .heading{color:var(--blush)}
.price-list{list-style:none;font-size:9.6px;line-height:16px;color:var(--ink-soft)}
.menu--light .price-list{color:#f4f4f4}
.price-list li{display:flex;align-items:baseline;white-space:nowrap}
.price-list .item{flex:none}
.price-list .leader{flex:1;border-bottom:1px dotted currentColor;margin:0 2px;transform:translateY(-3px);opacity:.7}
.price-list .price{flex:none}
.price-list .note-row{font-size:8.9px}
.note{font-size:8px;line-height:12px;color:var(--ink-soft);margin:4px 0 12px}
.footer-wide{position:absolute;left:0;top:496px;width:500.6px;height:33px;background:var(--blush);font-size:14px;display:flex;align-items:center;padding-left:15px;color:#222;z-index:2}
.footer-web{position:absolute;left:0;right:0;top:496px;height:33px;background:var(--blush);display:flex;align-items:center;justify-content:center;gap:6px;font-size:13.5px;color:#222}
.top-visual{position:absolute;left:57px;top:622px;width:501px;height:215px;z-index:1}
.circle-photo{position:absolute;z-index:2;left:388px;top:690px;width:156px;height:156px;border-radius:50%;border:5px solid var(--blush);background:radial-gradient(circle at 55% 45%,#f1d6c8,#cfa595 60%,#8f6c62);box-shadow:0 0 0 3px #fff}
</style>
</head>
<body>

<!-- Outside sheet -->
<section class="sheet sheet--outside" aria-label="Flyer outside">
  <article class="panel">
    <svg class="photo" style="left:0;top:0" width="251" height="230" viewBox="0 0 251 230" role="img" aria-label="Photo of smooth bare legs on a soft pink backdrop">
      <defs><linearGradient id="legs" x1="0" y1="0" x2="1" y2="1"><stop offset="0" stop-color="#f4e4df"/><stop offset=".5" stop-color="#e4bfae"/><stop offset="1" stop-color="#f1ded8"/></linearGradient></defs>
      <rect width="251" height="230" fill="url(#legs)"/>
      <path d="M0 0H140C90 10 40 40 0 95Z" fill="#fff" opacity=".85"/>
      <path d="M0 95C40 40 90 12 140 0H170C110 15 50 50 0 110Z" fill="#d9a89c"/>
    </svg>
    <div class="intro">
      <h2 class="heading">L U M O Medical Aesthetics</h2>
      <div class="copy justify">
        <p>We believe in providing only the best for our clients. We specialize in a number of Medical Aesthetics Treatments to address common skin and anti-aging concerns among our clients.</p>
        <p>All of our treatments are non-invasive, highly effective and affordable and our services are performed by certified professionals, using clinically proven equipment and products approved and certified through Civic Care Bureau.</p>
        <p>Many of which are award-winning devices and equipment that is recognized and respected, world-wide.</p>
      </div>
    </div>
    <div class="band">info@lumoclinica.example</div>
  </article>

  <article class="panel panel--slate">
    <svg class="photo" style="left:0;top:0" width="251" height="110" viewBox="0 0 251 110" aria-hidden="true">
      <path d="M0 0H251V78C170 50 90 60 0 95Z" fill="#f3f3f3"/>
      <path d="M0 95C90 60 170 50 251 78V84C170 58 90 68 0 101Z" fill="#d9a89c"/>
    </svg>
    <div class="photo" role="img" aria-label="Round portrait photo of a woman with skin treatment markings" style="left:67px;top:36px;width:118px;height:118px;border-radius:50%;border:4px solid var(--blush);box-shadow:0 0 0 3px #fff;background:radial-gradient(circle at 50% 45%,#f3ddd2,#d7b0a0 65%,#8a6a60)"></div>
    <div class="contact">
      <h2 class="heading">We’d love to hear from you</h2>
      <p class="copy">We take pride in the high calibre experience we offer our clients and believe that choosing the appropriate certified professional that can deliver the results you desire, is of primary importance. Lumo employs highly qualified professionals, operating under Dr. Daniel Okafor, Board Certified Plastic Surgeon acting as the Medical Director, as well as partners of the Harbourline Medical team.</p>
    </div>
    <div class="contact-rule"></div>
    <div class="team">Lena Marsh 555.014.3318<br>Maren Dahl 555.014.7720<br>Nadia Brooks 555.014.5096</div>
    <div class="more">For more information, visit us at<br>
      <svg width="10" height="10" viewBox="0 0 10 10" aria-hidden="true" style="vertical-align:-1px"><circle cx="5" cy="5" r="4" fill="none" stroke="#fff"/><path d="M1 5H9M5 1C3 3 3 7 5 9M5 1C7 3 7 7 5 9" fill="none" stroke="#fff" stroke-width=".7"/></svg>
      www.lumoclinica.example</div>
    <div class="social"><span>@lumoclinica</span><span>lumoclinica</span></div>
    <div class="band band--deep">
      <svg width="11" height="11" viewBox="0 0 12 12" aria-hidden="true"><circle cx="6" cy="6" r="5.3" fill="none" stroke="#222"/><path d="M4 3.2l1 1.4-.6.8c.5 1 1.2 1.7 2.2 2.2l.8-.6 1.4 1-.6 1c-2.5-.3-4.7-2.5-5-5z" fill="#222"/></svg>
      555-014-2271</div>
  </article>

  <article class="panel">
    <div class="brand brand--cover"><span class="brand-name">LUMO</span><span class="brand-sub">MEDICAL AESTHETICS</span></div>
    <svg class="photo" style="left:0;top:100px" width="251" height="300" viewBox="0 0 251 300" role="img" aria-label="Photo of a woman's face held by gloved hands">
      <defs><linearGradient id="face" x1="0" y1="0" x2="1" y2="1"><stop offset="0" stop-color="#3a2e2b"/><stop offset=".45" stop-color="#e8cbbd"/><stop offset="1" stop-color="#f4f1f0"/></linearGradient></defs>
      <path d="M0 40C90 20 170 10 251 0V255C170 275 90 290 0 300Z" fill="url(#face)"/>
      <path d="M0 40C90 20 170 10 251 0" fill="none" stroke="#d9a89c" stroke-width="4"/>
      <path d="M0 300C90 290 170 275 251 255" fill="none" stroke="#d9a89c" stroke-width="3"/>
    </svg>
    <h2 class="heading tagline">Laser hair removal, Nuvexa,<br>dermal fillers, microblading,<br>lashes and more</h2>
    <div class="band">www.lumoclinica.example</div>
  </article>
</section>

<!-- Inside sheet -->
<svg class="top-visual" viewBox="0 0 501 215" role="img" aria-label="Photo of a client receiving a facial skin treatment with a microneedling pen">
  <defs><linearGradient id="spa" x1="0" y1="0" x2="1" y2=".4"><stop offset="0" stop-color="#f3f3f3"/><stop offset=".35" stop-color="#e9cdbd"/><stop offset=".7" stop-color="#f0e6e2"/><stop offset="1" stop-color="#eeeeee"/></linearGradient></defs>
  <path d="M0 0H501V175C330 150 160 165 0 200Z" fill="url(#spa)"/>
  <path d="M0 200C160 165 330 150 501 175V182C330 162 160 176 0 215Z" fill="#8f8f91"/>
</svg>
<div class="circle-photo" role="img" aria-label="Round photo of eyelash extensions being applied"></div>

<section class="sheet sheet--inside" aria-label="Flyer inside">
  <article class="panel">
    <div class="menu" style="top:250px">
      <h3 class="heading">Neuromodulator/Toxin</h3>
      <ul class="price-list">
        <li><span class="item">Velanor</span><span class="leader"></span><span class="price">$8/unit</span></li>
        <li><span class="item">Nuvexa</span><span class="leader"></span><span class="price">$10/unit</span></li>
      </ul>
      <h3 class="heading" style="margin-top:14px">Dermal Filler</h3>
      <p class="note" style="margin-bottom:20px">cheeks, lips, jawline, chin, temples, under eyes, smile lines, smokers lines)</p>
      <ul class="price-list">
        <li><span class="item">1ml Syringe</span><span class="leader"></span><span class="price">$475</span></li>
        <li><span class="item">Mini Lip Plump</span><span class="leader"></span><span class="price">$250</span></li>
        <li><span class="item">Non-Surgical Face Lift</span><span class="leader"></span><span class="price">$1100</span></li>
      </ul>
      <p class="note">(Choice of 3 areas, eg. lips, jaw contouring, cheeks)</p>
    </div>
  </article>

  <article class="panel">
    <div class="menu" style="top:250px">
      <h3 class="heading">Facial Treatments:</h3>
      <ul class="price-list">
        <li><span class="item">Personalized Facial</span><span class="leader"></span><span class="price">$85</span></li>
        <li><span class="item">Organic Facial</span><span class="leader"></span><span class="price">$100</span></li>
        <li><span class="item">Deep Cleansing / Acne Facial</span><span class="leader"></span><span class="price">$120</span></li>
        <li><span class="item">Gel Peel (20% Glycolic/10% Lactic/3.2pH)</span><span class="leader"></span><span class="price">$75</span></li>
        <li><span class="item">Dermaplaning</span><span class="leader"></span><span class="price">$120</span></li>
        <li><span class="item">Microdermabrasion</span><span class="leader"></span><span class="price">$120</span></li>
        <li><span class="item">Microneedling</span><span class="leader"></span><span class="price">$250</span></li>
        <li><span class="item">Microneedling Package of 3</span><span class="leader"></span><span class="price">$600</span></li>
        <li><span class="item">Platelet-Rich Plasma (PRP) Facial</span><span class="leader"></span><span class="price">$400</span></li>
        <li class="note-row"><span class="item">Platinum Facial (Dermaplaning + Microneedling)</span><span class="leader"></span><span class="price">$350</span></li>
        <li><span class="item">LED Light Therapy</span><span class="leader"></span><span class="price">$45</span></li>
        <li><span class="item">High Frequency</span><span class="leader"></span><span class="price">$45</span></li>
        <li><span class="item">Skin Consultation</span><span class="leader"></span><span class="price">(Free)</span></li>
      </ul>
    </div>
  </article>

  <article class="panel panel--slate">
    <div class="brand brand--light"><span class="brand-name">LUMO</span><span class="brand-sub">MEDICAL AESTHETICS</span></div>
    <div class="menu menu--light" style="top:66px">
      <h3 class="heading">Medical Aesthetics Treatments</h3>
      <ul class="price-list">
        <li class="note-row"><span class="item">Laser Hair Removal</span><span class="leader"></span><span class="price">$35 and up per session</span></li>
        <li class="note-row"><span class="item">(Consultation and patch test required for all clients)</span></li>
        <li class="note-row"><span class="item">Microneedling for Stretch Marks and Scars</span><span class="leader"></span><span class="price">$250 +</span></li>
        <li class="note-row"><span class="item">Platelet-Rich Plasma (PRP) Hair Restoration</span><span class="leader"></span><span class="price">$500</span></li>
        <li class="note-row"><span class="item">Scalp Micropigmentation</span><span class="leader"></span><span class="price">$500 and up</span></li>
      </ul>
    </div>
    <div class="menu menu--light" style="top:189px">
      <h3 class="heading">Permanent Make-Up</h3>
      <ul class="price-list">
        <li><span class="item">Microblading</span><span class="leader"></span><span class="price">$350</span></li>
        <li><span class="item">Microblading Touch-Up</span><span class="leader"></span><span class="price">$50</span></li>
        <li><span class="item">Lashline Enhancement- Top Lashline</span><span class="leader"></span><span class="price">$300</span></li>
        <li><span class="item">Lashline Enhancement- Bottom Lashline</span><span class="leader"></span><span class="price">$350</span></li>
        <li><span class="item">Touch-Up Top/Bottom Lashline</span><span class="leader"></span><span class="price">$50</span></li>
        <li><span class="item">Lip Blush</span><span class="leader"></span><span class="price">$450</span></li>
        <li><span class="item">Lip Blush Touch-up</span><span class="leader"></span><span class="price">$50</span></li>
        <li><span class="item">Tattoo Removal</span><span class="leader"></span><span class="price">$200 per session</span></li>
      </ul>
    </div>
    <div class="menu menu--light" style="top:358px">
      <h3 class="heading">Cosmetic Treatments</h3>
      <ul class="price-list">
        <li><span class="item">Classic Eyelash Extensions</span><span class="leader"></span><span class="price">$99</span></li>
        <li><span class="item">Classic Fill</span><span class="leader"></span><span class="price">$45</span></li>
        <li><span class="item">Hybrid Eyelash Extensions</span><span class="leader"></span><span class="price">$120</span></li>
        <li><span class="item">Hybrid Fill</span><span class="leader"></span><span class="price">$55</span></li>
        <li><span class="item">Eyelash Lift &amp; Tint</span><span class="leader"></span><span class="price">$75</span></li>
        <li><span class="item">Teeth Whitening</span><span class="leader"></span><span class="price">$125</span></li>
        <li><span class="item">Organic Teeth Whitening</span><span class="leader"></span><span class="price">$150</span></li>
      </ul>
    </div>
    <div class="footer-web">
      <svg width="11" height="11" viewBox="0 0 10 10" aria-hidden="true"><circle cx="5" cy="5" r="4" fill="none" stroke="#222"/><path d="M1 5H9M5 1C3 3 3 7 5 9M5 1C7 3 7 7 5 9" fill="none" stroke="#222" stroke-width=".7"/></svg>
      www.lumoclinica.example</div>
  </article>
  <div class="footer-wide">Please get in touch for an informal chat or for a free care assessment.</div>
</section>

</body>
</html>
```